We need a website so we can post future events of our company about business motivation. The site have to include a calendar on the "Home" page that when the user cliks on the day of the event , there should open a small page with the information of the event (location,time,subject of the event...) . We need also an "About Us" page with information about our company and what we do as well as "Contact" page with our email and phone number and access to our facebook page. We would like to have a private access for users ("Restricted access") but they have to put their e-mail and password to access the special page (log in). On the 'special page' we would like to have some videos and photos that we will post on that page regularly .
Here is a website that would be an exemple of how we would like to have ours
http://northvalecapitalhub.example
The needs to be responsed and with backoffice

Industry/Entity Type

Business

Number of Pages Required

3 page

Colors
9bcb3c
f37122

Requirements
Must have
• Must have a restricted access page so the user can place a user name and a secret password.

```html
<!DOCTYPE html>
<html lang="en">
<head>
<meta charset="utf-8">
<title>Summit Drive – About Us</title>
<link href="https://fonts.googleapis.com/css2?family=Open+Sans:ital,wght@0,400;0,600;0,700;1,400&family=Arimo:wght@400;700&display=swap" rel="stylesheet">
<style>
  :root {
    --header-bg: #333333;
    --offers-bg: #ebeae8;
    --quote-bg: #f8f8f8;
    --footer-bg: #414042;
    --bottom-bg: #2b2b2b;
    --orange: #f37122;
    --green: #9bcb3c;
    --ink: #3a3a3a;
    --text: #555555;
    --white: #ffffff;
    --line: #8a8a8a;
  }
  * { margin: 0; padding: 0; box-sizing: border-box; }
  html, body { width: 1200px; height: 2462px; overflow: hidden; }
  body { position: relative; background: var(--white); font-family: "Open Sans", Arial, sans-serif; color: var(--text); }

  /* Header */
  .site-header { position: absolute; left: 0; top: 0; width: 1200px; height: 138px; background: var(--header-bg); }
  .brand { position: absolute; left: 90px; top: 42px; display: flex; align-items: center; gap: 12px;
           font-family: "Arimo", Arial, sans-serif; font-weight: 700; font-size: 29px; color: var(--white); letter-spacing: 0.5px; }
  .brand-mark { width: 22px; height: 22px; background: var(--green); }
  .main-nav a { position: absolute; top: 92px; font-family: "Arimo", Arial, sans-serif; font-size: 17px; color: var(--white); text-decoration: none; }
  .main-nav a.active::after { content: ""; position: absolute; left: 0; right: 0; bottom: -11px; height: 2px; background: var(--white); }
  .account { position: absolute; left: 975px; top: 88px; font-size: 16px; color: #cccccc; }
  .account .login { color: var(--green); }
  .account .register { color: var(--orange); }

  /* Section headings */
  .section-heading { position: absolute; left: 98px; color: var(--ink); font-weight: 400; }
  .section-heading::before { content: ""; position: absolute; left: 0; top: -13px; width: 24px; height: 3px; background: var(--orange); }
  .section-heading .kicker { display: block; font-size: 21px; line-height: 26px; font-weight: 400; text-transform: uppercase; }
  .section-heading .title { display: block; font-size: 35px; line-height: 40px; font-weight: 700; text-transform: uppercase; }

  .photo { position: absolute; }

  /* Story */
  .story-text { position: absolute; left: 507px; top: 322px; width: 652px; font-size: 16px; line-height: 27.5px; color: var(--text); }
  .story-quote { position: absolute; left: 507px; top: 515px; width: 650px; height: 120px; border: 1px solid var(--line); }
  .story-quote svg { position: absolute; left: 11px; top: -8px; background: var(--white); }
  .story-quote p { position: absolute; left: 48px; top: 29px; width: 580px; font-size: 15.5px; line-height: 27px; font-style: italic; color: var(--text); }

  /* Offers */
  .offers { position: absolute; left: 0; top: 768px; width: 1200px; height: 542px; background: var(--offers-bg); }
  .offer-title { position: absolute; top: 910px; font-size: 17px; font-weight: 700; letter-spacing: 0.6px; color: var(--ink); text-transform: uppercase; }
  .offer-text { position: absolute; top: 940px; width: 290px; font-size: 16.5px; line-height: 28px; color: var(--text); }
  .offer-list { position: absolute; top: 1040px; list-style: none; font-size: 16.5px; line-height: 35px; color: var(--text); }
  .offer-list li::before { content: ">"; font-size: 12px; margin-right: 12px; position: relative; top: -1px; }
  .btn-details { position: absolute; top: 1210px; width: 194px; height: 64px; background: var(--orange); color: var(--white);
                 font-size: 16px; font-weight: 700; letter-spacing: 1px; display: flex; align-items: center; justify-content: center; text-decoration: none; }

  /* Testimonials */
  .testimonials { position: absolute; left: 0; top: 1310px; width: 1200px; height: 658px; background: var(--quote-bg); }
  .testimonial-text { position: absolute; top: 1748px; width: 290px; font-size: 14px; line-height: 17px; color: var(--text); }
  .testimonial-name { position: absolute; top: 1815px; font-size: 16px; line-height: 21px; font-weight: 700; letter-spacing: 1px; color: var(--ink); text-transform: uppercase; }

  /* Footer */
  .site-footer { position: absolute; left: 0; top: 1968px; width: 1200px; height: 391px; background: var(--footer-bg); }
  .footer-title { position: absolute; top: 2042px; font-family: "Arimo", Arial, sans-serif; font-size: 21px; font-weight: 400; color: var(--white); }
  .footer-links { position: absolute; left: 98px; top: 2119px; list-style: none; font-family: "Arimo", Arial, sans-serif; font-size: 17px; line-height: 35px; }
  .footer-links a { color: var(--white); text-decoration: none; }
  .footer-about { position: absolute; left: 366px; top: 2122px; width: 230px; font-family: "Arimo", Arial, sans-serif; font-size: 16px; line-height: 21px; font-weight: 700; color: var(--white); }
  .gallery-thumb { position: absolute; width: 90px; height: 90px; }
  .bottom-bar { position: absolute; left: 0; top: 2359px; width: 1200px; height: 103px; background: var(--bottom-bg); }
  .copyright { position: absolute; left: 98px; top: 2398px; font-family: "Arimo", Arial, sans-serif; font-size: 17px; color: var(--white); }
</style>
</head>
<body>

<header class="site-header">
  <div class="brand"><span class="brand-mark"></span>SUMMIT DRIVE</div>
  <nav class="main-nav">
    <a href="#" style="left:355px">HOME</a>
    <a href="#" class="active" style="left:471px">ABOUT US</a>
    <a href="#" style="left:617px">CALENDAR</a>
    <a href="#" style="left:768px">CONTACT</a>
  </nav>
  <div class="account"><span class="login">Log in</span>&nbsp;&nbsp;or&nbsp;&nbsp;<span class="register">Register</span></div>
</header>

<!-- Our story -->
<h2 class="section-heading" style="top:240px"><span class="kicker">Our</span><span class="title">Story</span></h2>
<div class="photo" role="img" aria-label="Wooden lectern with two microphones in front of a blurred audience"
     style="left:39px;top:332px;width:422px;height:305px;background:linear-gradient(135deg,#2a3560 0%,#6e5d55 40%,#c9b9a5 60%,#8a6a40 100%);"></div>
<p class="story-text">Lorem Ipsum is simply dummy text of the printing and typesetting industry. Lorem Ipsum has been the industry's standard dummy text ever since the 1500s, when an unknown printer took a galley of type and scrambled it to make a type specimen book. It has survived not only five centuries, but also the leap into electronic typesetting, remaining essentially unchanged. It was popularised in the 1960s with the release of</p>
<blockquote class="story-quote">
  <svg width="34" height="20" viewBox="0 0 34 20" aria-hidden="true">
    <g fill="#444"><circle cx="11" cy="12" r="5"/><path d="M6 12 Q6 5 12 3 L12 5 Q8 7 8 12Z"/>
    <circle cx="24" cy="12" r="5"/><path d="M19 12 Q19 5 25 3 L25 5 Q21 7 21 12Z"/></g>
  </svg>
  <p>Started at 1980 Ipsum is simply dummy text of the printing and typesetting industry. Lorem Ipsum has been the industry's standard dummy.</p>
</blockquote>

<!-- Offers -->
<section class="offers"></section>
<h2 class="section-heading" style="top:813px"><span class="kicker">Our</span><span class="title">Offers</span></h2>

<div class="photo" role="img" aria-label="Large conference hall filled with audience under purple stage lights"
     style="left:39px;top:916px;width:220px;height:220px;background:linear-gradient(160deg,#6a3aa0 0%,#b23a80 45%,#d8b58a 70%,#6b3a2a 100%);"></div>
<h3 class="offer-title" style="left:294px">Lorem Ipsum Sit Amet</h3>
<p class="offer-text" style="left:294px">Lorem Ipsum is simply dummy text of the printing and typesetting industry. Lorem Ipsum has been.</p>
<ul class="offer-list" style="left:294px">
  <li>Lorem Ipsum is simply dummy.</li>
  <li>Discovered the undoubtable.</li>
  <li>Various versions have evolved.</li>
  <li>Discovered the undoubtable.</li>
</ul>
<a class="btn-details" href="#" style="left:295px">VIEW DETAILS</a>

<div class="photo" role="img" aria-label="Speaker on stage with large projection screens in a dark auditorium"
     style="left:629px;top:913px;width:204px;height:205px;background:linear-gradient(150deg,#3a2a22 0%,#a46a4a 40%,#2a2a30 70%,#141418 100%);"></div>
<h3 class="offer-title" style="left:867px">Lorem Ipsum</h3>
<p class="offer-text" style="left:867px">Lorem Ipsum is simply dummy text of the printing and typesetting industry. Lorem Ipsum has been.</p>
<ul class="offer-list" style="left:867px">
  <li>Lorem Ipsum is simply dummy.</li>
  <li>Discovered the undoubtable.</li>
  <li>Various versions have evolved.</li>
  <li>Discovered the undoubtable.</li>
</ul>
<a class="btn-details" href="#" style="left:868px">VIEW DETAILS</a>

<!-- Testimonials -->
<section class="testimonials"></section>
<h2 class="section-heading" style="top:1422px"><span class="kicker">Testemonial</span><span class="title">Quote</span></h2>

<div class="photo" role="img" aria-label="Black and white portrait of the first client" style="left:97px;top:1535px;width:138px;height:199px;background:linear-gradient(180deg,#2a2a2a,#8a8a8a 55%,#1c1c1c);"></div>
<div class="photo" role="img" aria-label="Black and white portrait of the second client" style="left:442px;top:1535px;width:135px;height:199px;background:linear-gradient(180deg,#111,#7a7a7a 55%,#151515);"></div>
<div class="photo" role="img" aria-label="Black and white portrait of the third client" style="left:783px;top:1533px;width:169px;height:200px;background:linear-gradient(180deg,#555,#9a9a9a 55%,#444);"></div>

<p class="testimonial-text" style="left:97px">I couldn't go back to the traditional business world now, not after experiencing how great this is.</p>
<p class="testimonial-name" style="left:97px">Sam Harlow,<br>Senior Vice President. C.O.C</p>
<p class="testimonial-text" style="left:441px">I couldn't go back to the traditional business world now, not after experiencing how great this is.</p>
<p class="testimonial-name" style="left:441px">Sam Harlow,<br>Senior Vice President. C.O.C</p>
<p class="testimonial-text" style="left:782px">I couldn't go back to the traditional business world now, not after experiencing how great this is.</p>
<p class="testimonial-name" style="left:782px">Sam Harlow,<br>Senior Vice President. C.O.C</p>

<!-- Footer -->
<footer class="site-footer"></footer>
<h4 class="footer-title" style="left:98px">Quick links</h4>
<h4 class="footer-title" style="left:371px">About Us</h4>
<h4 class="footer-title" style="left:950px">Gallery</h4>
<ul class="footer-links">
  <li><a href="#">HOME</a></li>
  <li><a href="#">ABOUT US</a></li>
  <li><a href="#">CALENDAR</a></li>
  <li><a href="#">CONTACT</a></li>
</ul>
<p class="footer-about">Lorem ipsum dolor sit amet, consectetur adipiscing elit, sed do eiusmod tempor incididunt ut labore et dolore magna aliqua.</p>

<div class="gallery-thumb" role="img" aria-label="Event photo: speaker and screens" style="left:739px;top:2118px;background:linear-gradient(150deg,#3a2a22,#a46a4a,#1a1a1e);"></div>
<div class="gallery-thumb" role="img" aria-label="Event photo: conference hall" style="left:844px;top:2118px;background:linear-gradient(160deg,#6a3aa0,#b23a80,#d8b58a);"></div>
<div class="gallery-thumb" role="img" aria-label="Event photo: audience in blue light" style="left:949px;top:2118px;background:linear-gradient(160deg,#2a2a70,#5a5ac0,#1a1a40);"></div>
<div class="gallery-thumb" role="img" aria-label="Event photo: presenter on stage" style="left:1054px;top:2118px;background:linear-gradient(160deg,#4aa0d0,#2a6a90,#c46a3a);"></div>
<div class="gallery-thumb" role="img" aria-label="Event photo: speaker and screens" style="left:739px;top:2224px;background:linear-gradient(150deg,#3a2a22,#a46a4a,#1a1a1e);"></div>
<div class="gallery-thumb" role="img" aria-label="Event photo: conference hall" style="left:844px;top:2224px;background:linear-gradient(160deg,#6a3aa0,#b23a80,#d8b58a);"></div>
<div class="gallery-thumb" role="img" aria-label="Event photo: audience in blue light" style="left:949px;top:2224px;background:linear-gradient(160deg,#2a2a70,#5a5ac0,#1a1a40);"></div>
<div class="gallery-thumb" role="img" aria-label="Event photo: presenter on stage" style="left:1054px;top:2224px;background:linear-gradient(160deg,#4aa0d0,#2a6a90,#c46a3a);"></div>

<div class="bottom-bar"></div>
<p class="copyright">© 2016 Summit Drive, All Right Reserved.</p>

</body>
</html>
```